Design a Framework Graphic for Our Online YouTube Course

We have created a system/framework to help teach our students one of our main concepts. We teach content creators and business owners how to grow on YouTube.
We made a rough outline of how we'd like the framework to look. So we'd at least like this made into a better image, cleaned up and made more cohesive. But we're also interested in seeing other creative ways of visualizing the framework. It could be designed in several different ways. Most important things are showing the process of going through each of these steps, and then repeating it over and over again.
1. Reverse Engineering
2. Research
3. Record
4. Release
5. Rocket - this is the pinnacle moment and we want to emphasize it
6. Review - (it's wrong on the attached image)
7. Repeat
The original vision was to show the first 3 steps as "ramping" up to the release time, then the rocket visual, then the rest is done and it circles back to step 1.
We want it to be something our students could print out an put on their wall. Something memorable that will help them memorize the system.
We also need an icon that can represent each step. The icon doesn't necessarily have to be on the master framework graphic, but we need these icons for use in the rest of our materials. We'd like simple, black and white graphic icons that represent each step.
Use the color red in the photo and we can send you the "Clip Summit Institute" logo if you need.
Target Market(s)
Beginner to advanced content creators and business owners who want to learn how to grow on YouTube
Font styles to use
Other font styles liked:
- Helvetica Neue is our brand font
Look and feel

```html
<!DOCTYPE html>
<html lang="en">
<head>
<meta charset="utf-8">
<title>Seven Step Growth Framework</title>
<link rel="stylesheet" href="https://fonts.googleapis.com/css2?family=Inter:wght@700&display=swap">
<style>
  :root {
    --bg: #222124;
    --red: #e8202a;
    --white: #ffffff;
  }
  html, body {
    margin: 0;
    padding: 0;
    background: var(--bg);
    overflow: hidden;
  }
  .framework {
    position: relative;
    width: 1200px;
    height: 675px;
    background: var(--bg);
    overflow: hidden;
    font-family: "Inter", "Helvetica Neue", Arial, sans-serif;
  }
  .framework-art {
    position: absolute;
    inset: 0;
    width: 1200px;
    height: 675px;
  }
  .step {
    position: absolute;
    height: 37px;
    box-sizing: border-box;
    padding: 0 10px;
    display: flex;
    align-items: center;
    gap: 9px;
    background: var(--red);
    border-radius: 9px;
    color: var(--white);
    font-weight: 700;
    font-size: 19px;
    letter-spacing: 0.1px;
    white-space: nowrap;
  }
  .step-number {
    width: 25px;
    height: 25px;
    border-radius: 50%;
    background: var(--white);
    color: var(--red);
    font-size: 16px;
    display: flex;
    align-items: center;
    justify-content: center;
    flex: none;
  }
  .step--reverse  { left: 281px; top: 475px; width: 213px; }
  .step--research { left: 575px; top: 475px; width: 141px; }
  .step--record   { left: 797px; top: 475px; width: 122px; }
  .step--release  { left: 912px; top: 319px; width: 125px; }
  .step--rocket   { left: 725px; top: 162px; width: 125px; }
  .step--review   { left: 350px; top: 162px; width: 125px; }
  .step--repeat   { left: 162px; top: 319px; width: 125px; }
</style>
</head>
<body>
<main class="framework">
  <svg class="framework-art" viewBox="0 0 1920 1080" fill="none" stroke-linejoin="round" stroke-linecap="round" aria-hidden="true">
    <defs>
      <g id="rocket-icon">
        <path d="M1790,375 L1833,440 L1828,632 L1752,632 L1745,440 Z" stroke="var(--red)" stroke-width="4"/>
        <path d="M1748,440 Q1790,430 1832,440" stroke="var(--white)" stroke-width="4"/>
        <circle cx="1790" cy="490" r="28" stroke="var(--white)" stroke-width="4"/>
        <path d="M1750,505 L1706,585 L1706,610 L1752,620" stroke="var(--red)" stroke-width="4"/>
        <path d="M1830,505 L1874,585 L1874,610 L1828,620" stroke="var(--red)" stroke-width="4"/>
        <path d="M1770,644 L1810,644 M1780,632 L1778,644 M1800,632 L1802,644" stroke="var(--white)" stroke-width="4"/>
        <path d="M1772,650 Q1766,690 1790,705 Q1814,690 1808,650" stroke="var(--red)" stroke-width="4"/>
        <path d="M1781,650 Q1782,682 1790,688 Q1798,682 1799,650" stroke="var(--white)" stroke-width="4"/>
      </g>
    </defs>

    <!-- loop path -->
    <rect class="loop" x="360" y="290" width="1200" height="500" rx="85" stroke="var(--red)" stroke-width="10"/>

    <!-- review: monitor -->
    <g class="icon-review">
      <rect x="549" y="63" width="221" height="142" stroke="var(--red)" stroke-width="4"/>
      <rect x="557" y="71" width="205" height="126" stroke="var(--white)" stroke-width="4"/>
      <path d="M637,205 L637,216 M683,205 L683,216" stroke="var(--white)" stroke-width="4"/>
      <rect x="625" y="216" width="70" height="10" rx="4" stroke="var(--red)" stroke-width="4"/>
      <rect x="574" y="156" width="14" height="22" stroke="var(--red)" stroke-width="4"/>
      <rect x="593" y="120" width="14" height="58" stroke="var(--white)" stroke-width="4"/>
      <rect x="612" y="143" width="14" height="35" stroke="var(--red)" stroke-width="4"/>
      <rect x="631" y="128" width="14" height="50" stroke="var(--white)" stroke-width="4"/>
      <rect x="650" y="108" width="14" height="70" stroke="var(--red)" stroke-width="4"/>
      <path d="M580,112 L600,98 L620,106 L658,88" stroke="var(--red)" stroke-width="4"/>
      <circle cx="715" cy="133" r="32" stroke="var(--white)" stroke-width="4"/>
      <path d="M715,133 L722,102 A32,32 0 0 1 745,124 Z" stroke="var(--red)" stroke-width="4"/>
    </g>

    <!-- rocket: launching -->
    <use href="#rocket-icon" transform="translate(1262,145) rotate(45) scale(0.6) translate(-1790,-540)"/>

    <!-- release: rocket standing -->
    <use href="#rocket-icon"/>

    <!-- repeat: cycle arrows -->
    <g class="icon-repeat">
      <path d="M198,520 A70,70 0 0 0 72,505" stroke="var(--red)" stroke-width="5"/>
      <path d="M47,515 L84,495 L62,536 Z" stroke="var(--red)" stroke-width="5"/>
      <path d="M62,560 A70,70 0 0 0 188,575" stroke="var(--white)" stroke-width="5"/>
      <path d="M214,565 L177,585 L199,544 Z" stroke="var(--white)" stroke-width="5"/>
    </g>

    <!-- reverse engineer: gear with arrow -->
    <g class="icon-reverse">
      <circle cx="628" cy="950" r="40" stroke="var(--white)" stroke-width="14" stroke-dasharray="14 17"/>
      <circle cx="628" cy="950" r="34" stroke="var(--white)" stroke-width="4"/>
      <circle cx="628" cy="950" r="48" stroke="var(--white)" stroke-width="3" stroke-dasharray="14 17" opacity="0"/>
      <path d="M560,955 A72,72 0 1 1 700,960" stroke="var(--red)" stroke-width="5"/>
      <path d="M538,950 L575,952 L558,975 Z" stroke="var(--red)" stroke-width="4"/>
      <path d="M695,975 A72,72 0 0 1 565,985" stroke="var(--red)" stroke-width="6" stroke-dasharray="16 8"/>
    </g>

    <!-- research: document with magnifier -->
    <g class="icon-research">
      <path d="M958,875 L1040,875 L1072,907 L1072,1025 L958,1025 Z" stroke="var(--red)" stroke-width="4"/>
      <path d="M1040,875 L1040,907 L1072,907" stroke="var(--red)" stroke-width="4"/>
      <rect x="970" y="958" width="14" height="22" stroke="var(--white)" stroke-width="4"/>
      <rect x="989" y="945" width="14" height="35" stroke="var(--red)" stroke-width="4"/>
      <rect x="1008" y="935" width="14" height="45" stroke="var(--white)" stroke-width="4"/>
      <rect x="970" y="992" width="34" height="8" stroke="var(--red)" stroke-width="4"/>
      <rect x="970" y="1005" width="34" height="8" stroke="var(--white)" stroke-width="4"/>
      <circle cx="1048" cy="968" r="35" stroke="var(--red)" stroke-width="4"/>
      <circle cx="1048" cy="968" r="26" stroke="var(--white)" stroke-width="4"/>
      <path d="M1074,995 L1100,1022 L1108,1014 L1082,988" stroke="var(--red)" stroke-width="4"/>
    </g>

    <!-- record: video camera -->
    <g class="icon-record">
      <rect x="1290" y="905" width="120" height="90" rx="10" stroke="var(--red)" stroke-width="5"/>
      <circle cx="1350" cy="950" r="18" stroke="var(--red)" stroke-width="5"/>
      <path d="M1410,935 L1455,913 L1455,986 L1410,963" stroke="var(--red)" stroke-width="5"/>
    </g>
  </svg>

  <div class="step step--reverse"><span class="step-number">1</span>Reverse Engineer</div>
  <div class="step step--research"><span class="step-number">2</span>Research</div>
  <div class="step step--record"><span class="step-number">3</span>Record</div>
  <div class="step step--release"><span class="step-number">4</span>Release</div>
  <div class="step step--rocket"><span class="step-number">5</span>Rocket</div>
  <div class="step step--review"><span class="step-number">6</span>Review</div>
  <div class="step step--repeat"><span class="step-number">7</span>Repeat</div>
</main>
</body>
</html>
```